Business Card and Stationary for Maplecrest Baptist Day School
Maplecrest Baptist Day School
Business Card and Stationary for Maplecrest Baptist Day School - Childcare
Creative Brief
Bright & Fun-filled
Delia Fenwick
Day School Director
4817 W. Tollbridge Rd Hampton, VA 23671
dayschool@maplecrestbaptistexample.com
www.MCDaySchool-example.com
Walking in Faith, Growing Hearts, Nurturing Spirits (See uploaded logo) Theme Verse is: Luke 2:52 And Jesus increased in wisdom and stature, and in favour with God and man.
Hours of Operation: Monday - Friday 6am - 6pm See attached QR Code

```html
<!DOCTYPE html>
<html lang="en">
<head>
<meta charset="utf-8">
<title>Maplecrest Baptist Day School – Business Card</title>
<link rel="stylesheet" href="https://fonts.googleapis.com/css2?family=Oswald:wght@500;600&family=Open+Sans:wght@400;600&display=swap">
<style>
  :root {
    --bg: #eef0f2;
    --card: #ffffff;
    --navy: #1f1d4e;
    --swoosh: #c9cbd3;
    --ink-muted: #7a7d88;
    --white: #ffffff;
    --brand: #2c8fc9;
  }
  * { margin: 0; padding: 0; box-sizing: border-box; }
  html, body { width: 1200px; height: 492px; overflow: hidden; }
  body {
    background: var(--bg);
    font-family: "Open Sans", sans-serif;
    display: flex; align-items: center; justify-content: center;
  }
  .business-card {
    position: relative;
    width: 700px; height: 400px;
    background: var(--card);
    box-shadow: 0 6px 24px rgba(0,0,0,.12);
    overflow: hidden;
  }
  .card-band { position: absolute; inset: 0; }
  .brand {
    position: absolute; left: 44px; top: 40px; width: 260px;
    text-align: center;
  }
  .brand-tagline {
    font-size: 11px; color: var(--brand); font-weight: 600;
    margin-bottom: 14px;
  }
  .brand-mark {
    display: flex; align-items: center; justify-content: center; gap: 10px;
  }
  .brand-dot { width: 22px; height: 22px; border-radius: 50%; background: var(--brand); flex: none; }
  .brand-name {
    font-family: "Oswald", sans-serif; font-weight: 600;
    font-size: 24px; line-height: 1.1; color: var(--brand); text-align: left;
  }
  .holder {
    position: absolute; right: 44px; top: 56px; text-align: right;
  }
  .holder-name {
    font-family: "Oswald", sans-serif; font-weight: 600;
    font-size: 30px; letter-spacing: .5px; color: var(--navy);
    text-transform: uppercase;
  }
  .holder-title { font-size: 12px; color: var(--ink-muted); margin-top: 2px; }
  .hours {
    position: absolute; right: 44px; top: 200px; color: var(--white);
    font-family: "Oswald", sans-serif;
  }
  .hours-heading { font-size: 22px; font-weight: 600; text-transform: uppercase; letter-spacing: .5px; }
  .hours-days { font-size: 18px; font-weight: 500; margin-top: 4px; text-align: center; }
  .hours-time { font-size: 18px; font-weight: 500; text-align: center; }
  .contact {
    position: absolute; left: 44px; bottom: 36px; list-style: none;
    color: var(--white); font-size: 12px;
  }
  .contact li { display: flex; align-items: center; gap: 10px; margin-top: 8px; }
  .contact svg { width: 14px; height: 14px; flex: none; fill: var(--white); }
</style>
</head>
<body>
  <article class="business-card">
    <svg class="card-band" viewBox="0 0 700 400" preserveAspectRatio="none" aria-hidden="true">
      <path d="M0 232 C 220 170, 470 150, 700 110 L700 128 C 470 168, 220 190, 0 252 Z" fill="var(--swoosh)"/>
      <path d="M0 262 C 220 198, 470 176, 700 136 L700 400 L0 400 Z" fill="var(--navy)"/>
    </svg>

    <div class="brand">
      <p class="brand-tagline">Walking in Faith, Growing Hearts, Nurturing Spirits</p>
      <div class="brand-mark">
        <span class="brand-dot"></span>
        <span class="brand-name">Maplecrest Baptist<br>Day School</span>
      </div>
    </div>

    <header class="holder">
      <h1 class="holder-name">Delia Fenwick</h1>
      <p class="holder-title">Day School Director</p>
    </header>

    <section class="hours">
      <h2 class="hours-heading">Hours of Operation</h2>
      <p class="hours-days">Monday - Friday</p>
      <p class="hours-time">6 am - 6 pm</p>
    </section>

    <ul class="contact">
      <li>
        <svg viewBox="0 0 24 24"><path d="M12 2a7 7 0 0 0-7 7c0 5 7 13 7 13s7-8 7-13a7 7 0 0 0-7-7zm0 9.5A2.5 2.5 0 1 1 12 6.5a2.5 2.5 0 0 1 0 5z"/></svg>
        4817 W. Tollbridge Rd Hampton, VA 23671
      </li>
      <li>
        <svg viewBox="0 0 24 24"><path d="M2 5h20v14H2zm2 2v.5l8 5 8-5V7zm0 2.8V17h16V9.8l-8 5z"/></svg>
        dayschool@maplecrestbaptistexample.com
      </li>
      <li>
        <svg viewBox="0 0 24 24"><path d="M12 2a10 10 0 1 0 0 20 10 10 0 0 0 0-20zm6.9 9h-3a15 15 0 0 0-1.3-5.6A8 8 0 0 1 18.9 11zM12 4.1c.9 1.2 1.8 3.6 1.9 6.9h-3.8c.1-3.3 1-5.7 1.9-6.9zM9.4 5.4A15 15 0 0 0 8.1 11h-3a8 8 0 0 1 4.3-5.6zM5.1 13h3a15 15 0 0 0 1.3 5.6A8 8 0 0 1 5.1 13zm6.9 6.9c-.9-1.2-1.8-3.6-1.9-6.9h3.8c-.1 3.3-1 5.7-1.9 6.9zm2.6-1.3a15 15 0 0 0 1.3-5.6h3a8 8 0 0 1-4.3 5.6z"/></svg>
        www.MCDaySchool-example.com
      </li>
    </ul>
  </article>
</body>
</html>
```